Weightloss company needs Business Card

We want a business card that is clean and professional, yet portrays that we are a friendly, innovative, and versatile program designed to fit the needs of our clients.
I would like there to be 2 sides, one side having an appointment card, and the other side containing the logo and business information. There can be decorations on both sides. The logo is attached.

Target Market(s)

Men and women 40-60

Industry/Entity Type

Business

Contact Information for Business Card

Font styles to use
Sans Serif

Requirements
Must have
• The logo, space for business information
Nice to have
• The colors in the logo
Should not have
• No pictures of people or food

```html
<!DOCTYPE html>
<html lang="en">
<head>
<meta charset="utf-8">
<title>Renewturn Wellness – Business Card</title>
<link rel="stylesheet" href="https://fonts.googleapis.com/css2?family=Open+Sans:wght@400;600;700&display=swap">
<style>
  :root {
    --brand-red: #e61e32;
    --brand-blue: #55c3ea;
    --ink: #1f1f1f;
    --card: #ffffff;
    --backdrop: #ecebe8;
    --rule: #333333;
  }
  * { box-sizing: border-box; margin: 0; padding: 0; }
  html, body { width: 1200px; height: 1000px; overflow: hidden; }
  body {
    background: var(--backdrop);
    font-family: "Open Sans", Arial, sans-serif;
    color: var(--ink);
    position: relative;
  }
  .card {
    position: absolute;
    left: 265px;
    width: 667px;
    height: 397px;
    background: var(--card);
    border-radius: 22px;
    overflow: hidden;
    box-shadow: 0 4px 14px rgba(0,0,0,0.18);
  }
  .card--front { top: 73px; }
  .card--back { top: 532px; }

  .wordmark {
    position: absolute;
    display: flex;
    align-items: center;
    gap: 12px;
    color: var(--brand-red);
    font-weight: 700;
    font-size: 34px;
    line-height: 1;
    white-space: nowrap;
  }
  .wordmark__dot {
    width: 22px; height: 22px;
    border-radius: 50%;
    background: var(--brand-blue);
    flex: none;
  }
  .card--front .wordmark { right: 40px; top: 108px; }
  .card--back .wordmark { right: 40px; top: 82px; }

  .person { position: absolute; left: 33px; top: 183px; }
  .person__name { color: var(--brand-red); font-weight: 700; font-size: 22px; line-height: 1.2; }
  .person__role { font-size: 16px; margin-top: 2px; }

  .contacts { position: absolute; left: 33px; top: 249px; list-style: none; }
  .contacts li {
    display: flex; align-items: center; gap: 7px;
    font-size: 16.5px; line-height: 23px;
  }
  .contacts svg { width: 14px; height: 14px; fill: var(--brand-red); flex: none; }

  .address {
    position: absolute; right: 34px; top: 268px;
    text-align: right; font-size: 16.5px; line-height: 23px; font-style: normal;
  }

  .wave { position: absolute; left: 0; bottom: 0; width: 667px; height: 100px; display: block; }

  .appointment__title {
    position: absolute; left: 33px; top: 111px;
    color: var(--brand-red); font-weight: 700; font-size: 18px; letter-spacing: 0.3px;
  }
  .appointment__fields {
    position: absolute; left: 33px; top: 208px; width: 602px;
    display: flex; gap: 8px; font-size: 17px;
  }
  .field { display: flex; align-items: flex-end; gap: 8px; }
  .field__line { border-bottom: 1px solid var(--rule); height: 16px; }
  .field--time .field__line { width: 246px; }
  .field--date .field__line { width: 246px; }

  .days {
    position: absolute; left: 33px; top: 256px; width: 602px;
    display: flex; justify-content: space-between; list-style: none; font-size: 17px;
  }
  .days li { display: flex; align-items: center; gap: 10px; }
  .days li::after {
    content: ""; width: 17px; height: 17px;
    border: 2px solid var(--brand-red); border-radius: 50%;
  }
  .appointment__notice {
    position: absolute; left: 33px; top: 299px; font-size: 17.4px; white-space: nowrap;
  }
</style>
</head>
<body>

<section class="card card--front" aria-label="Business card front">
  <div class="wordmark"><span>Renewturn Wellness</span><span class="wordmark__dot"></span></div>

  <div class="person">
    <p class="person__name">Daniel Morgan</p>
    <p class="person__role">Managing Director</p>
  </div>

  <ul class="contacts">
    <li><svg viewBox="0 0 14 14"><rect x="3.5" y="0.5" width="7" height="13" rx="1.5"/><rect x="5" y="2.5" width="4" height="5" fill="#fff"/></svg>+ 000 000 0000</li>
    <li><svg viewBox="0 0 14 14"><path d="M1 5 Q7 0 13 5 L11 7 L9 5 L5 5 L3 7Z"/><rect x="2.5" y="7" width="9" height="6" rx="1"/></svg>+ 000 000 0000</li>
    <li><svg viewBox="0 0 14 14"><rect x="0.5" y="2.5" width="13" height="9" rx="1"/><path d="M1 3 L7 8 L13 3" stroke="#fff" stroke-width="1.2" fill="none"/></svg>info@renewturnwellness.com</li>
    <li><svg viewBox="0 0 14 14"><circle cx="7" cy="7" r="6.5"/><path d="M0.5 7 H13.5 M7 0.5 V13.5" stroke="#fff" stroke-width="1"/></svg>www.renewturnwellness.com</li>
  </ul>

  <address class="address">1840 Maplecrest Avenue,<br>Fairview Park, IL 60451</address>

  <svg class="wave" viewBox="0 0 667 100" preserveAspectRatio="none" aria-hidden="true">
    <path d="M0 38 C70 72 250 100 430 90 C540 84 610 40 667 34 L667 100 L0 100Z" fill="var(--brand-blue)"/>
    <path d="M0 68 C150 98 320 100 450 88 C550 78 620 52 667 48 L667 100 L0 100Z" fill="#fff"/>
    <path d="M0 73 C150 103 320 104 450 92 C550 82 620 57 667 53 L667 100 L0 100Z" fill="var(--brand-red)"/>
  </svg>
</section>

<section class="card card--back" aria-label="Appointment card">
  <div class="wordmark"><span>Renewturn Wellness</span><span class="wordmark__dot"></span></div>

  <h2 class="appointment__title">APPOINTMENT</h2>

  <div class="appointment__fields">
    <div class="field field--time"><span>Time:</span><span class="field__line"></span></div>
    <div class="field field--date"><span>Date:</span><span class="field__line"></span></div>
  </div>

  <ul class="days">
    <li>Mon</li><li>Tue</li><li>Wed</li><li>Thur</li><li>Fri</li><li>Sat</li>
  </ul>

  <p class="appointment__notice">If you are unable to keep your appointment , please allow 24 hours notice</p>

  <svg class="wave" viewBox="0 0 667 100" preserveAspectRatio="none" aria-hidden="true">
    <path d="M0 38 C70 72 250 100 430 90 C540 84 610 40 667 34 L667 100 L0 100Z" fill="var(--brand-blue)"/>
    <path d="M0 68 C150 98 320 100 450 88 C550 78 620 52 667 48 L667 100 L0 100Z" fill="#fff"/>
    <path d="M0 73 C150 103 320 104 450 92 C550 82 620 57 667 53 L667 100 L0 100Z" fill="var(--brand-red)"/>
  </svg>
</section>

</body>
</html>
```